Visual Print Advert for Hair & Makeup Artist

One page colour visual advertisement required for a hair and makeup artist business using pictures and logo with brief description and contact details. MUST have plain white background. All information will be provided I just need someone to put it in a good layout.
Professional, clean and appealing to the eye. Don't want it to look over crowded or busy.
Layout should feature 2-7 photos, without making the page look too busy. Can use any of the photos provided and you are welcome to crop them to change the orientation of the photo.
Content and typeface should fit in with logo and be modern but appeal to the female target audience of brides in Australia aged 22-40yo.
Advertisement is be be used in a bridal magazine and other print media for business advertising purposes.
Updates

Target Market(s)

Future brides in Australia aged 22 - 40yo - females only

Industry/Entity Type

Business

Colors
e34197
ffffff
eda3c7

Requirements
Must have
• White background
Should not have
• NO script writing as it doesn't fit with the logo.

```html
<!DOCTYPE html>
<html lang="en">
<head>
<meta charset="utf-8">
<title>Belvina Makeup Artistry – Bridal Advert</title>
<link href="https://fonts.googleapis.com/css2?family=Open+Sans:wght@300;400;600;700&display=swap" rel="stylesheet">
<style>
  :root {
    --brand-pink: #e34197;
    --soft-pink: #eda3c7;
    --white: #ffffff;
    --ink: #2b2b2b;
    --deep-green: #123a1e;
  }
  * { margin: 0; padding: 0; box-sizing: border-box; }
  html, body { width: 848px; height: 1200px; overflow: hidden; background: var(--white); }
  body { font-family: "Open Sans", Arial, sans-serif; }

  .advert { position: relative; width: 848px; height: 1200px; background: var(--white); overflow: hidden; }

  .header-band { position: absolute; left: 0; top: 0; width: 848px; height: 272px; background: var(--brand-pink); }
  .header-tab {
    position: absolute; left: 42px; top: 244px; width: 764px; height: 60px;
    background: var(--white); border-radius: 16px 16px 0 0;
  }

  .brand-name {
    position: absolute; left: 0; width: 848px; top: 40px; padding-left: 40px; text-align: center;
    font-weight: 300; font-size: 72px; letter-spacing: 40px; line-height: 1;
    color: var(--ink);
  }
  .brand-descriptor {
    position: absolute; right: 163px; top: 113px;
    font-weight: 300; font-size: 19px; letter-spacing: 5px; line-height: 1.3; color: var(--ink);
  }

  .headline {
    position: absolute; left: 0; width: 848px; top: 148px; text-align: center;
    color: var(--white); font-size: 37px; line-height: 44px; font-weight: 400;
  }
  .headline strong { font-weight: 600; }

  .experience {
    position: absolute; left: 0; width: 848px; top: 250px; text-align: center;
    color: var(--brand-pink); font-size: 45px; font-weight: 400; line-height: 1.2;
  }

  .photo { position: absolute; }
  .photo--bride-garden {
    left: 85px; top: 318px; width: 346px; height: 566px;
    background: radial-gradient(ellipse 70% 60% at 48% 62%, #f4f1ea 0%, #dfe3cf 22%, #8cbf5a 48%, #3c8a2a 70%, #1c4f1c 100%);
  }
  .photo--bride-bouquet {
    left: 446px; top: 318px; width: 347px; height: 369px;
    background: radial-gradient(ellipse 55% 70% at 52% 58%, #f3efe4 0%, #e6dcc6 30%, #b9b88c 58%, #6f7a45 82%, #3e4726 100%);
  }
  .photo--bridal-party {
    left: 444px; top: 696px; width: 351px; height: 188px;
    background: linear-gradient(180deg, #8f969c 0%, #c7b5a4 28%, #e3cbb8 50%, #8a7d74 72%, #2a2a30 100%);
  }

  .tagline {
    position: absolute; left: 0; width: 848px; top: 902px; text-align: center;
    color: var(--brand-pink); font-size: 26px; line-height: 32px;
  }
  .tagline strong { color: var(--deep-green); font-weight: 600; }

  .phone-box {
    position: absolute; left: 166px; top: 982px; width: 516px; height: 94px;
    background: var(--brand-pink); border-radius: 14px;
  }
  .phone-box__frame {
    position: absolute; inset: 9px 10px; border: 3px dotted var(--white); border-radius: 9px;
  }
  .phone-box__content {
    position: absolute; inset: 0; display: flex; align-items: center; justify-content: center; gap: 14px;
    color: var(--white); font-size: 52px; font-weight: 600; letter-spacing: 0.5px;
  }
  .phone-box__icon { width: 42px; height: 42px; }

  .contact-email {
    position: absolute; left: 0; width: 848px; top: 1086px; text-align: center;
    color: var(--brand-pink); font-size: 26px;
  }
  .contact-web {
    position: absolute; left: 0; width: 848px; top: 1136px; text-align: center;
    color: var(--ink); font-size: 26px; letter-spacing: 0.3px;
  }
</style>
</head>
<body>
<main class="advert">
  <div class="header-band"></div>
  <div class="header-tab"></div>

  <div class="brand-name">BELVINA</div>
  <div class="brand-descriptor">MAKEUP ARTISTRY</div>

  <h1 class="headline">PROFESSIONALLY <strong>TRAINED AND CERTIFIED</strong><br>MOBILE HAIR &amp; MAKEUP ARTISTS</h1>
  <p class="experience">with over 10 years experience</p>

  <div class="photo photo--bride-garden" role="img" aria-label="Bride in a white gown with a floral crown, standing in a green garden"></div>
  <div class="photo photo--bride-bouquet" role="img" aria-label="Red-haired bride in a lace dress holding a neutral-toned bouquet outdoors"></div>
  <div class="photo photo--bridal-party" role="img" aria-label="Bride smiling with her bridesmaids in dark dresses"></div>

  <p class="tagline">We specialise in naturally <strong>ENHANCING YOUR BEAUTY</strong><br>to have you looking and feeling your best on your special day.</p>

  <div class="phone-box">
    <div class="phone-box__frame"></div>
    <div class="phone-box__content">
      <svg class="phone-box__icon" viewBox="0 0 42 42" aria-hidden="true">
        <circle cx="21" cy="21" r="20" fill="var(--white)"/>
        <path d="M14 10c1.5-1 3-.5 3.6.8l2 4.2c.5 1-.1 2-.9 2.6l-1.6 1.1c1 2.8 3.3 5.6 6 7.2l1.3-1.4c.7-.8 1.8-1 2.7-.4l3.8 2.5c1.1.8 1.3 2.2.4 3.4-1.600 2.2-4 3-6.3 2-6.5-2.8-11.4-8.6-12.6-15.5-.4-2.6.9-5.1 1.6-6.5z" fill="var(--brand-pink)"/>
      </svg>
      <span>0400 123 456</span>
    </div>
  </div>

  <p class="contact-email">mia@belvinamakeup.com.au</p>
  <p class="contact-web">www.belvinamakeup.com.au</p>
</main>
</body>
</html>
```